Looking for an amazing business card for a thriving DJ business

We need a business card design for a DJ company based in South Florida. The DJ company specializes in weddings, parties, bar mitzvahs, corporate events, proms, and reunions. We are looking for a modern, simple business card design. The card should state DJ Marlow K.
Updates

The name on the card should be DJ Marlow K

Industry/Entity Type

Entertainment Industry

Contact Information for Business Card

DJ Marlow K
512.447.2086
atxdjmarlowk@quellmail.com
https://www.facebook.com/DjMarlowK/
https://www.instagram.com/djmarlow.k/
www.djmarlowk.net

Font styles to use
Serif
Sans Serif

Requirements
Must have
• My business card has to be awesome.
Should not have
• The card has to have personality.

```html
<!DOCTYPE html>
<html lang="en">
<head>
<meta charset="utf-8">
<title>DJ Marlow K — Business Card</title>
<link rel="stylesheet" href="https://fonts.googleapis.com/css2?family=Didact+Gothic&family=Roboto:wght@400&display=swap">
<style>
  :root {
    --page: #3a3330;
    --card: #1b2029;
    --card-deep: #151921;
    --art-light: #2e333c;
    --art-dark: #20242c;
    --ink: #f4f5f7;
    --ink-soft: #d9dce1;
  }
  * { margin: 0; padding: 0; box-sizing: border-box; }
  html, body { width: 1200px; height: 822px; overflow: hidden; }
  body {
    background: var(--page);
    position: relative;
    font-family: "Roboto", sans-serif;
    color: var(--ink);
  }
  .card {
    position: absolute;
    top: 256px;
    width: 525px;
    height: 310px;
    background: linear-gradient(135deg, var(--card) 0%, var(--card-deep) 100%);
    border-radius: 4px;
    box-shadow: 0 14px 30px rgba(0,0,0,.35);
    overflow: hidden;
  }
  .card--front { left: 45px; }
  .card--back { left: 630px; }

  .headphone-art {
    position: absolute;
    right: 20px;
    top: 20px;
    width: 190px;
    height: 270px;
    border-radius: 48% 48% 40% 40%;
    background: radial-gradient(ellipse at 40% 35%, var(--art-light) 0%, var(--art-dark) 70%, transparent 100%);
    opacity: .9;
  }

  .front-name {
    position: absolute;
    left: 140px;
    top: 82px;
    font-family: "Didact Gothic", sans-serif;
    font-size: 40px;
    font-weight: 400;
    letter-spacing: .5px;
    color: var(--ink);
    white-space: nowrap;
  }
  .front-rule {
    position: absolute;
    left: 0;
    right: 0;
    top: 196px;
    display: flex;
    align-items: center;
    gap: 12px;
  }
  .front-rule::before,
  .front-rule::after {
    content: "";
    height: 2px;
    background: var(--ink-soft);
  }
  .front-rule::before { width: 185px; }
  .front-rule::after { flex: 1; }
  .front-url {
    font-size: 12px;
    color: var(--ink-soft);
    white-space: nowrap;
  }

  .back-bar {
    position: absolute;
    left: 40px;
    top: 72px;
    width: 6px;
    height: 118px;
    background: var(--ink);
    border-radius: 3px;
  }
  .back-name {
    position: absolute;
    left: 62px;
    top: 66px;
    font-family: "Didact Gothic", sans-serif;
    font-size: 30px;
    font-weight: 400;
    color: var(--ink);
    white-space: nowrap;
  }
  .contact-list {
    position: absolute;
    left: 62px;
    top: 112px;
    list-style: none;
    font-size: 14px;
    line-height: 19px;
    color: var(--ink-soft);
  }
  .contact-list li { display: flex; align-items: center; gap: 8px; white-space: nowrap; }
  .contact-icon { width: 11px; height: 11px; flex: none; }
  .contact-mark {
    width: 10px; height: 10px; flex: none;
    background: var(--ink-soft);
    border-radius: 2px;
  }
</style>
</head>
<body>
  <section class="card card--front">
    <div class="headphone-art" role="img" aria-label="Faint headphones and music note illustration"></div>
    <h1 class="front-name">DJ Marlow K</h1>
    <div class="front-rule"><span class="front-url">www.djmarlowk.net</span></div>
  </section>

  <section class="card card--back">
    <div class="headphone-art" role="img" aria-label="Faint headphones and music note illustration"></div>
    <div class="back-bar"></div>
    <h2 class="back-name">DJ Marlow K</h2>
    <ul class="contact-list">
      <li>
        <svg class="contact-icon" viewBox="0 0 24 24" aria-hidden="true"><path fill="#d9dce1" d="M6.6 10.8a15 15 0 0 0 6.6 6.6l2.2-2.2a1 1 0 0 1 1-.25 11.4 11.4 0 0 0 3.6.6 1 1 0 0 1 1 1V20a1 1 0 0 1-1 1A17 17 0 0 1 3 4a1 1 0 0 1 1-1h3.5a1 1 0 0 1 1 1c0 1.25.2 2.450.6 3.6a1 1 0 0 1-.25 1z"/></svg>
        512.447.2086
      </li>
      <li>
        <svg class="contact-icon" viewBox="0 0 24 24" aria-hidden="true"><rect x="2" y="5" width="20" height="14" rx="1" fill="#d9dce1"/><path d="M2 6l10 7 10-7" stroke="#1b2029" stroke-width="2" fill="none"/></svg>
        atxdjmarlowk@quellmail.com
      </li>
      <li><span class="contact-mark"></span>www.fanpagehub.net/DjMarlowK</li>
      <li><span class="contact-mark"></span>www.snapgrid.net/djmarlow.k</li>
    </ul>
  </section>
</body>
</html>
```